Business Card Design

We are looking for a business card designed for our landscaping company. We do landscaping installation & Maintenance Services. We would like to see designs that have basic landscaping in background. We also think it is important to have both of our names and phone numbers on the card. We need something that stands out a little whether it is shape of the card or thickness or design.

Industry/Entity Type

Business

Contact Information for Business Card

Pale Ridge Yardworks, paleridgeyardworks@mailbrook.net, Dale Purvine 555-213-7690, Martin Kolbey 555-864-1037

```html
<!DOCTYPE html>
<html lang="en">
<head>
<meta charset="utf-8">
<title>Pale Ridge Yardworks — Business Card</title>
<link rel="stylesheet" href="https://fonts.googleapis.com/css2?family=Libre+Baskerville:wght@400;700&display=swap">
<style>
  :root {
    --backdrop: #ececec;
    --card-white: #ffffff;
    --sky-blue: #7f9fcf;
    --sky-blue-light: #93acd8;
    --leaf-green: #a6d77c;
    --divider-green: #8fcf6a;
    --grass-dark: #556b34;
    --grass-mid: #6d7f41;
    --grass-light: #7f8a4a;
    --ink: #141414;
    --ink-soft: #2a2a2a;
  }
  html, body {
    margin: 0;
    padding: 0;
    width: 1200px;
    height: 720px;
    overflow: hidden;
    background: var(--backdrop);
  }
  .card {
    position: absolute;
    left: 224px;
    top: 141px;
    width: 752px;
    height: 438px;
    background: var(--card-white);
    overflow: hidden;
    font-family: "Libre Baskerville", "Baskerville", Georgia, serif;
    color: var(--ink);
  }
  .sky-band {
    position: absolute;
    left: 0; top: 0;
    width: 100%; height: 57px;
    background: linear-gradient(90deg, var(--sky-blue) 0%, var(--sky-blue-light) 50%, var(--sky-blue) 100%);
  }
  .leaf-stripe {
    position: absolute;
    left: 0; top: 57px;
    width: 100%; height: 8px;
    background: var(--leaf-green);
  }
  .leaf-band {
    position: absolute;
    left: 0; top: 325px;
    width: 100%; height: 20px;
    background: var(--leaf-green);
  }
  .lawn {
    position: absolute;
    left: 0; top: 345px;
    width: 100%; height: 93px;
    background: linear-gradient(180deg, var(--grass-light) 0%, var(--grass-mid) 45%, var(--grass-dark) 100%);
  }
  .company-name {
    position: absolute;
    left: 40px;
    top: 154px;
    width: 296px;
    margin: 0;
    text-align: center;
    font-size: 29px;
    font-weight: 700;
    line-height: 41px;
  }
  .divider {
    position: absolute;
    left: 375px;
    top: 98px;
    width: 2px;
    height: 195px;
    background: var(--divider-green);
  }
  .contact {
    position: absolute;
    left: 433px;
    top: 0;
    font-size: 16.5px;
  }
  .contact-line {
    position: absolute;
    left: 0;
    margin: 0;
    white-space: nowrap;
    line-height: 1;
  }
  .email { top: 112px; color: var(--ink-soft); font-size: 15.5px; }
  .partner-name { color: var(--ink-soft); }
  .partner-phone { font-weight: 700; }
  .p1-name { top: 155px; }
  .p1-phone { top: 187px; }
  .p2-name { top: 230px; }
  .p2-phone { top: 262px; }
</style>
</head>
<body>
  <div class="card">
    <div class="sky-band"></div>
    <div class="leaf-stripe"></div>

    <h1 class="company-name">Pale Ridge<br>Yardworks</h1>

    <div class="divider"></div>

    <div class="contact">
      <p class="contact-line email">paleridgeyardworks@mailbrook.net</p>
      <p class="contact-line partner-name p1-name">Dale Purvine</p>
      <p class="contact-line partner-phone p1-phone">555-213-7690</p>
      <p class="contact-line partner-name p2-name">Martin Kolbey</p>
      <p class="contact-line partner-phone p2-phone">555-864-1037</p>
    </div>

    <div class="leaf-band"></div>
    <div class="lawn" role="img" aria-label="Photograph of a mowed green lawn"></div>
  </div>
</body>
</html>
```